Online bill payment portal website design

Online Invoice Payment Website

The customer will click on the logos of the institution they want to pay and the payment will be made at the latest stage to write the customer number.

Invoice payment can be made online. Telephone, Television, Internet, Electricity, Water, Natural Gas, and all institutional payments.

Example website : https://www.selvopay.com/

Industry/Entity Type

Invoice

Logo Text

KolayBorcKapat.Net

Number of Pages Required

4 page

Font styles to use
Serif
Sans Serif

Colors
abd036
33a6d7
876aae
e667a6
ec1f27
f37122
85abd2
0555a3
00a990

Requirements
Must have
• Logos of payment institutions
• Credit Card Payment form
• Customer information form
• COntact page
• List of Institutions
• Accept privacy policies in all forms
Nice to have
• Good and new design :)
Should not have
• Same with selvopay.com ! i want new site

```html
<!DOCTYPE html>
<html lang="en">
<head>
<meta charset="utf-8">
<title>Odevarim – Just Pay the Bill</title>
<link href="https://fonts.googleapis.com/css2?family=Open+Sans:wght@400;600;700;800&display=swap" rel="stylesheet">
<style>
:root{
  --brand:#2a3f9e;
  --ink:#333;
  --muted:#666;
  --white:#fff;
  --footer-bg:#f4f4f4;
  --line:#d6d6d6;
  --search:#33a6d7;
  --submit:#f37122;
  --tel:#abd036;
  --tv:#e667a6;
  --net:#33a6d7;
  --elec:#f37122;
  --water:#00a990;
  --gas:#876aae;
  --other:#85abd2;
  --badge:#c4c4c4;
}
*{box-sizing:border-box;margin:0;padding:0}
html,body{width:1200px;height:1127px;overflow:hidden;background:var(--white)}
body{position:relative;font-family:"Open Sans",Arial,sans-serif;color:var(--ink)}
.abs{position:absolute}

.site-header{position:absolute;left:0;top:0;width:1200px;height:98px;background:var(--white)}
.brand{position:absolute;left:92px;top:26px;font-size:36px;font-weight:800;color:var(--brand);letter-spacing:-0.5px}
.main-nav a{position:absolute;top:43px;font-size:16px;color:var(--ink);text-decoration:none;letter-spacing:.2px}
.login-btn{position:absolute;left:1017px;top:36px;width:95px;height:34px;border:1.5px solid var(--ink);border-radius:17px;font-size:16px;text-align:center;line-height:31px;color:var(--ink)}

.hero{position:absolute;left:0;top:98px;width:1200px;height:465px;overflow:hidden}
.hero-photo{position:absolute;inset:0;background:
  radial-gradient(ellipse 260px 300px at 790px 220px,#5b6470 0%,rgba(90,98,110,0) 70%),
  linear-gradient(100deg,#7c8087 0%,#6a6e74 35%,#54585f 60%,#75797f 100%)}
.hero-shade{position:absolute;inset:0;background:rgba(40,44,50,.28)}
.hero-title{position:absolute;left:0;top:88px;width:1200px;text-align:center;font-size:43px;font-weight:400;color:var(--white);letter-spacing:.5px}
.search-box{position:absolute;left:247px;top:186px;width:613px;height:58px;background:var(--white);border-radius:3px 0 0 3px}
.search-btn{position:absolute;left:860px;top:186px;width:109px;height:58px;background:var(--search);color:var(--white);font-size:17px;text-align:center;line-height:58px;border-radius:0 3px 3px 0}

.bill-tile{position:absolute;top:359px;width:130px;height:106px;border-radius:3px 3px 0 0;color:var(--white);text-align:center;box-shadow:0 2px 4px rgba(0,0,0,.18)}
.bill-tile svg{position:absolute;left:45px;top:20px;width:40px;height:40px}
.bill-tile span{position:absolute;left:0;right:0;top:70px;font-size:14px;letter-spacing:.2px}
.t-tel{left:99px;background:var(--tel)}
.t-tv{left:245px;background:var(--tv)}
.t-net{left:391px;background:var(--net)}
.t-elec{left:537px;background:var(--elec)}
.t-water{left:683px;background:var(--water)}
.t-gas{left:829px;background:var(--gas)}
.t-other{left:975px;background:var(--other)}

.agencies-title{position:absolute;left:0;top:615px;width:1200px;text-align:center;font-size:20px;color:var(--ink)}
.agency-card{position:absolute;width:215px;height:67px;background:var(--white);border:1px solid #dcdcdc;box-shadow:0 1px 4px rgba(0,0,0,.15)}
.agency-card i{position:absolute;left:62px;top:20px;width:90px;height:26px;background:var(--badge);border-radius:3px}

.site-footer{position:absolute;left:0;top:887px;width:1200px;height:240px;background:var(--footer-bg)}
.footer-brand{position:absolute;left:101px;top:68px;font-size:31px;font-weight:800;color:var(--brand);letter-spacing:-0.5px}
.footer-head{position:absolute;font-size:15px;color:var(--ink);letter-spacing:.2px}
.footer-links{position:absolute;left:371px;top:70px;list-style:none}
.footer-links li{font-size:12px;color:#555;height:24px;line-height:24px}
.footer-links li::before{content:"»";margin-right:5px}
.mail-note{position:absolute;left:614px;top:71px;width:210px;font-size:12px;line-height:17px;color:#555}
.mail-input{position:absolute;left:613px;top:115px;width:147px;height:31px;background:var(--white);border:1px solid #ccc;font-size:13px;color:#666;line-height:29px;padding-left:9px}
.mail-submit{position:absolute;left:760px;top:115px;width:57px;height:31px;background:var(--submit);color:var(--white);font-size:13px;line-height:31px;text-align:center}
.social-dot{position:absolute;top:79px;width:24px;height:24px;background:#444;border-radius:4px}
.pay-card{position:absolute;top:123px;width:33px;height:22px;background:#d9d9d9;border-radius:2px}
.footer-rule{position:absolute;left:86px;top:184px;width:1022px;height:1px;background:var(--line)}
.copyright{position:absolute;left:0;top:207px;width:1200px;text-align:center;font-size:13px;color:var(--ink)}
</style>
</head>
<body>

<header class="site-header">
  <div class="brand">Odevarim</div>
  <nav class="main-nav">
    <a style="left:548px">HOME</a>
    <a style="left:648px">ABOUT US</a>
    <a style="left:778px">SUPPORTS</a>
    <a style="left:910px">CONTACTS</a>
  </nav>
  <div class="login-btn">LOGIN</div>
</header>

<section class="hero">
  <div class="hero-photo" role="img" aria-label="Blurred photo of a hand holding a smartphone in an office"></div>
  <div class="hero-shade"></div>
  <h1 class="hero-title">JUST PAY THE BILL!</h1>
  <div class="search-box"></div>
  <div class="search-btn">SEARCH</div>

  <div class="bill-tile t-tel">
    <svg viewBox="0 0 40 40" fill="none" stroke="#fff" stroke-width="2.6"><rect x="11" y="2" width="18" height="36" rx="3"/><line x1="17" y1="33" x2="23" y2="33"/></svg>
    <span>TELEPHONE</span>
  </div>
  <div class="bill-tile t-tv">
    <svg viewBox="0 0 40 40" fill="none" stroke="#fff" stroke-width="3"><rect x="2" y="5" width="36" height="23" rx="2"/><path d="M15 30h10v4h5v3H10v-3h5z" fill="#fff" stroke="none"/></svg>
    <span>TELEVISION</span>
  </div>
  <div class="bill-tile t-net">
    <svg viewBox="0 0 40 40" fill="none" stroke="#fff" stroke-width="3.4" stroke-linecap="round"><path d="M3 15a24 24 0 0 1 34 0"/><path d="M9 21a16 16 0 0 1 22 0"/><path d="M15 27a8 8 0 0 1 10 0"/><circle cx="20" cy="33" r="2.5" fill="#fff" stroke="none"/></svg>
    <span>INTERNET</span>
  </div>
  <div class="bill-tile t-elec">
    <svg viewBox="0 0 40 40"><path d="M23 2L12 22h8l-4 16 13-22h-8z" fill="#fff"/></svg>
    <span>ELECTRICITY</span>
  </div>
  <div class="bill-tile t-water">
    <svg viewBox="0 0 40 40"><path d="M20 4C15 14 10 19 10 26a10 10 0 0 0 20 0c0-7-5-12-10-22z" fill="#fff"/><path d="M15 27a5 5 0 0 0 4 5" stroke="#00a990" stroke-width="2" fill="none"/></svg>
    <span>WATER</span>
  </div>
  <div class="bill-tile t-gas">
    <svg viewBox="0 0 40 40"><path d="M22 2c-8 8-11 14-11 20a9 9 0 0 0 15 6c-5 1-8-3-6-8 1-4 4-6 2-18z" fill="#fff"/><rect x="6" y="36" width="28" height="2" fill="#fff"/></svg>
    <span>NATURAL GAS</span>
  </div>
  <div class="bill-tile t-other">
    <svg viewBox="0 0 40 40" fill="#fff"><rect x="5" y="17" width="8" height="7" rx="1"/><rect x="16" y="17" width="8" height="7" rx="1"/><rect x="27" y="17" width="8" height="7" rx="1"/></svg>
    <span>OTHER</span>
  </div>
</section>

<h2 class="agencies-title" style="font-weight:400">OTHER CONTRACTED AGENCIES WILL BE ABLE TO PAY THE BILL</h2>
<div class="agency-card" style="left:142px;top:680px"><i></i></div>
<div class="agency-card" style="left:377px;top:680px"><i></i></div>
<div class="agency-card" style="left:610px;top:680px"><i></i></div>
<div class="agency-card" style="left:844px;top:680px"><i></i></div>
<div class="agency-card" style="left:140px;top:762px"><i></i></div>
<div class="agency-card" style="left:375px;top:762px"><i></i></div>
<div class="agency-card" style="left:609px;top:762px"><i></i></div>
<div class="agency-card" style="left:843px;top:762px"><i></i></div>

<footer class="site-footer">
  <div class="footer-brand">Odevarim</div>

  <div class="footer-head" style="left:371px;top:46px">MY ACCOUNT</div>
  <ul class="footer-links">
    <li>Privacy Policy</li>
    <li>Your Account</li>
    <li>Advanced Search</li>
    <li>Contact Us</li>
  </ul>

  <div class="footer-head" style="left:612px;top:43px">JOIN OUR MAILING LIST</div>
  <p class="mail-note">Your about us information would fit here nicely.</p>
  <div class="mail-input">Email address</div>
  <div class="mail-submit">Submit</div>

  <div class="footer-head" style="left:941px;top:43px">FOLLOW US OUT THERE</div>
  <span class="social-dot" style="left:942px"></span>
  <span class="social-dot" style="left:981px"></span>
  <span class="social-dot" style="left:1020px"></span>
  <span class="social-dot" style="left:1058px"></span>
  <span class="pay-card" style="left:940px"></span>
  <span class="pay-card" style="left:975px"></span>
  <span class="pay-card" style="left:1010px"></span>
  <span class="pay-card" style="left:1045px"></span>

  <div class="footer-rule"></div>
  <p class="copyright">Copyright © 2017. All Rights Reserved</p>
</footer>

</body>
</html>
```